MARINE ENGINE PARTS BIZ SITE NEED TOTAL REDESIGN

Re-design our current site: www.verodakmaritime.com.bd<br/>From the existing site you will have the idea, your creative site to be more attractive, modern and user friendly yet simple. Present version likeness is below 20%. It should be SEO Friendly. Mobile, Tablet and Desktop versions are necessary.<br/>Trust True Fittings, Stay Afloat- is our slogan to be highlighted and placed on a proper location.<br/>CONTACT US ** Form to be created, same section we shall provide pictures of the key contacts once design is approved<br/>CONTACT US ** Communication apps to be designed more professionally, Social media to be added, Testimonials to be added <br/>Target Market(s) / products <br/>Bangladesh for Local biz support and others for International Market, <br/>Product Separating to Local Biz and Intl biz is a good idea <br/>Colors<br/>Designer to stick to our brand colors and theme colors but reduce percentage of usage.<br/>Contents <br/>As it is can be finalized, your suggestions are most welcome, whoever comes with much better contents based on current format will be awarded an additional bonus of USD 150.00 by selecting as 2nd winner (Here we will provide SEO friendly words to rewrite some lines) <br/>Pictures<br/><br/>You may select few pictures from provided gallery and use in suitable places, <br/>Note : these are our own pictures other than designing this site copying is prohibited.<br/><br/>We are available for any discussion <br/><br/>best regards<br/>Oliver <br/><br/><br/><br/><br/>

Target Market(s)

International Shipping Sector

Coding

Coded - Design and coding required

Number of Pages Required

5+ page

Font styles to use
Other font styles liked:
• Any most popular SEO Friendly form, Book Antigua preferred but designer can select others

Colors

Designer to choose colors to be used in the design.

Requirements
Must have
• Environmental friendly these, Go green type
Nice to have
• Max usage of the pictures provided by us
Should not have
• Pictures from other sites, or from Internet

```html
<!DOCTYPE html>
<html lang="en">
<head>
<meta charset="utf-8">
<title>Verodak Maritime BD (Pvt.) Limited</title>
<link rel="stylesheet" href="https://fonts.googleapis.com/css2?family=Cinzel:wght@600&family=Libre+Baskerville:wght@400;700&display=swap">
<style>
:root{
  --green:#0b7a3e;
  --green-dark:#06602f;
  --green-deep:#054d26;
  --maroon:#8a1c2b;
  --ink:#333;
  --muted:#666;
  --white:#fff;
  --line:#d9d9d9;
}
*{box-sizing:border-box;margin:0;padding:0}
html,body{width:1200px;height:2888px;overflow:hidden}
body{font-family:"Libre Baskerville",Georgia,serif;color:var(--ink);background:var(--white);position:relative}
.abs{position:absolute}

/* top navigation */
.topbar{left:0;top:0;width:1200px;height:28px;background:var(--green-dark)}
.topbar .nav{left:130px;top:0;height:28px;display:flex;gap:34px;align-items:center;font-size:11px;color:var(--white);font-weight:700}
.topbar .nav span:first-child{background:var(--green);padding:8px 14px}
.socials{display:flex;gap:7px}
.socials i{display:block;width:22px;height:22px;border-radius:3px}
.topbar .socials{left:790px;top:3px}
.search{left:1005px;top:5px;width:80px;height:18px;background:var(--white);border-radius:2px;font-size:9px;color:#999;padding:3px 6px}
.search-btn{left:1085px;top:5px;width:20px;height:18px}

/* header */
.header{left:0;top:28px;width:1200px;height:68px;background:var(--white)}
.brand{left:135px;top:16px;display:flex;align-items:center;gap:10px;font-size:17px;font-weight:700;color:var(--maroon)}
.brand i{display:block;width:32px;height:32px;background:var(--maroon)}

/* hero */
.hero{left:0;top:96px;width:1200px;height:456px;background:linear-gradient(180deg,#5d7480 0%,#8a9aa2 35%,#4b5a5f 70%,#2f3b3f 100%)}
.hero-slogan{left:0;top:382px;width:1200px;text-align:center;font-family:"Cinzel",serif;font-size:34px;color:var(--white);letter-spacing:1px;text-shadow:0 2px 6px rgba(0,0,0,.5)}

/* about */
.about-photo{left:148px;top:608px;width:290px;height:380px;background:linear-gradient(160deg,#9bb08c,#6f8660 55%,#4a5b40)}
.about-corner{width:26px;height:26px;background:#c7d3c8}
.about-text{left:592px;top:660px;width:480px}
.eyebrow{font-size:11px;color:var(--green);font-weight:700;letter-spacing:1px}
.about-text h2{font-size:25px;color:var(--maroon);margin:6px 0 16px;line-height:1.2}
.about-text p{font-size:10.5px;line-height:1.75;color:var(--muted);margin-bottom:12px}
.btn{display:inline-block;background:var(--green);color:var(--white);font-size:11px;padding:8px 18px;border-radius:2px}
.btn-outline{display:inline-block;border:1px solid var(--white);color:var(--white);font-size:11px;padding:7px 16px;border-radius:2px}

/* business support band */
.support{left:0;top:1080px;width:1200px;height:320px;background:linear-gradient(180deg,var(--green) 0%,var(--green-dark) 100%)}
.support-col{top:70px;width:360px;text-align:center;color:var(--white)}
.support-col h3{font-size:15px;font-weight:700;margin:14px 0 10px}
.support-col p{font-size:10px;line-height:1.7;opacity:.9;margin-bottom:16px}
.divider{left:599px;top:60px;width:1px;height:220px;background:rgba(255,255,255,.35)}

/* products */
.section-title{width:1200px;left:0;text-align:center;font-size:26px;color:var(--maroon);font-weight:700}
.title-rule{left:570px;width:60px;height:2px;background:var(--green)}
.product{top:1560px;width:240px;text-align:center}
.product .shot{width:150px;height:120px;margin:0 auto 14px;border-radius:6px}
.product p{font-size:12px;color:var(--ink)}

/* testimonials */
.testimonials{left:0;top:1840px;width:1200px;height:400px;background:linear-gradient(180deg,var(--green) 0%,var(--green-dark) 100%)}
.testimonials .section-title{color:var(--white);top:70px}
.card{top:130px;width:300px;height:210px;background:var(--white);border-radius:4px;padding:18px 20px;box-shadow:0 3px 8px rgba(0,0,0,.2)}
.card .top{display:flex;justify-content:space-between;align-items:center}
.stars{color:#0b7a3e;font-size:14px;letter-spacing:2px}
.ago{font-size:9px;color:#999}
.card h4{font-size:12px;margin:12px 0 8px;color:var(--ink)}
.card p{font-size:10px;line-height:1.7;color:var(--muted)}
.card .who{position:absolute;left:20px;bottom:18px;display:flex;align-items:center;gap:8px;font-size:11px;color:var(--green);font-weight:700}
.card .who i{display:block;width:26px;height:26px;border-radius:50%;background:#cfd8d2}
.arrow{top:218px;width:30px;height:30px;border-radius:50%;background:var(--white)}

/* contact */
.contact{left:0;top:2240px;width:1200px;height:380px;background:linear-gradient(180deg,#f4f6f5 0%,#e3e8e6 100%)}
.contact .section-title{top:24px}
.contact .sub{left:0;top:76px;width:1200px;text-align:center;font-size:11px;color:var(--muted)}
.field{left:296px;width:300px;height:44px;background:var(--white);border:1px solid var(--line);border-radius:2px;font-size:10px;color:#999;padding:15px 14px}
.field .ic{position:absolute;right:12px;top:14px}
.message{left:612px;top:120px;width:300px;height:188px;background:var(--white);border:1px solid var(--line);border-radius:2px;font-size:10px;color:#999;padding:15px 14px}
.submit{left:530px;top:324px;width:140px;height:36px;background:var(--green-deep);color:var(--white);font-size:12px;font-weight:700;text-align:center;line-height:36px;letter-spacing:1px}

/* footer */
.footer{left:0;top:2620px;width:1200px;height:232px;background:linear-gradient(180deg,#eef1f0 0%,#dfe5e2 100%)}
.footer-nav{left:0;top:48px;width:1200px;display:flex;justify-content:center;gap:80px;font-size:11px;font-weight:700;color:var(--ink)}
.footer-rule{left:130px;top:84px;width:940px;height:1px;background:#c9d0cc}
.footer .brand{left:140px;top:116px}
.footer .socials{left:720px;top:122px}
.disclaimer{left:140px;top:188px;width:920px;font-size:9px;color:var(--muted);line-height:1.5}
.copyright{left:0;top:2852px;width:1200px;height:36px;background:var(--green-dark);color:var(--white);font-size:9px;text-align:center;line-height:36px}
</style>
</head>
<body>

<div class="abs topbar">
  <div class="abs nav"><span>HOME</span><span>ABOUT US</span><span>PRODUCTS &amp; STOCKS</span><span>CERTIFICATIONS &amp; QA</span><span>CONTACT US</span></div>
  <div class="abs socials">
    <i style="background:#1d6fa3"></i><i style="background:#3b5998"></i><i style="background:#c4302b"></i><i style="background:#2aa952"></i><i style="background:#7a4fa0"></i><i style="background:#2d9be0"></i><i style="background:#0a66c2"></i><i style="background:#d13f3f"></i>
  </div>
  <div class="abs search">Search here</div>
  <svg class="abs search-btn" viewBox="0 0 20 18"><circle cx="9" cy="8" r="4" fill="none" stroke="#fff" stroke-width="1.6"/><line x1="12" y1="11" x2="15" y2="14" stroke="#fff" stroke-width="1.6"/></svg>
</div>

<header class="abs header">
  <div class="abs brand"><i></i>VERODAK MARITIME BD (PVT.) LIMITED</div>
</header>

<section class="abs hero" role="img" aria-label="Cargo ships moored side by side in a harbour">
  <div class="abs hero-slogan">TRUST TRUE FITTINGS, STAY AFLOAT</div>
</section>

<section class="about">
  <div class="abs about-corner" style="left:136px;top:596px"></div>
  <div class="abs about-corner" style="left:424px;top:974px"></div>
  <div class="abs about-photo" role="img" aria-label="Smiling child standing near the shipyard"></div>
  <div class="abs about-text">
    <div class="eyebrow">ABOUT</div>
    <h2>VERODAK MARITIME BD (PVT.) LIMITED</h2>
    <p>We believe in corporate social responsibility and in practising sound business ethics, so we make sure every part we supply meets strict quality standards for lasting, safe and sustainable vessel operation.</p>
    <p>Over the last decade, many responsible shipowners have turned to reclaimed marine equipment, and we are proud to follow that path. With this approach we source genuine engine parts and reusable fittings from retired ships, inspect them carefully and recondition them to the highest standard before delivery to our clients.</p>
    <span class="btn">Read More</span>
  </div>
</section>

<section class="abs support">
  <div class="abs support-col" style="left:180px">
    <svg width="44" height="44" viewBox="0 0 44 44" role="img" aria-label="Map of Bangladesh"><circle cx="22" cy="22" r="18" fill="#fff"/></svg>
    <h3>LOCAL BUSINESS SUPPORT</h3>
    <p>We supply reconditioned engines, generators and spares to vessels and yards across Bangladesh with quick delivery and trusted after-sales care.</p>
    <span class="btn-outline">Know More</span>
  </div>
  <div class="abs divider"></div>
  <div class="abs support-col" style="left:660px">
    <svg width="44" height="44" viewBox="0 0 44 44"><circle cx="22" cy="22" r="18" fill="none" stroke="#fff" stroke-width="2.5"/><ellipse cx="22" cy="22" rx="8" ry="18" fill="none" stroke="#fff" stroke-width="2"/><line x1="4" y1="22" x2="40" y2="22" stroke="#fff" stroke-width="2"/></svg>
    <h3>INTERNATIONAL BUSINESS SUPPORT</h3>
    <p>We ship genuine marine parts to owners and operators worldwide, backed by careful inspection, clear documents and reliable export handling.</p>
    <span class="btn-outline">Know More</span>
  </div>
</section>

<section class="products">
  <h2 class="abs section-title" style="top:1498px">OUR PRODUCTS</h2>
  <div class="abs title-rule" style="top:1538px"></div>
  <div class="abs product" style="left:180px">
    <div class="shot" role="img" aria-label="Marine main engine" style="background:linear-gradient(160deg,#b9874a,#6e4a2a)"></div>
    <p>Main Engine</p>
  </div>
  <div class="abs product" style="left:480px">
    <div class="shot" role="img" aria-label="Auxiliary engine and generator set" style="background:linear-gradient(160deg,#3f7f6a,#1f3d34)"></div>
    <p>Auxiliary Engines / Generators</p>
  </div>
  <div class="abs product" style="left:780px">
    <div class="shot" role="img" aria-label="Assorted marine spare parts" style="background:linear-gradient(160deg,#8a8a8a,#3d3d3d)"></div>
    <p>Other Equipment and Parts</p>
  </div>
  <span class="abs btn-outline" style="left:552px;top:1756px;color:var(--green);border-color:var(--green)">Know More</span>
</section>

<section class="abs testimonials">
  <h2 class="abs section-title">TESTIMONIALS</h2>
  <svg class="abs arrow" style="left:118px" viewBox="0 0 30 30"><polyline points="17,9 11,15 17,21" fill="none" stroke="#0b7a3e" stroke-width="2"/></svg>
  <svg class="abs arrow" style="left:1052px" viewBox="0 0 30 30"><polyline points="13,9 19,15 13,21" fill="none" stroke="#0b7a3e" stroke-width="2"/></svg>
  <div class="abs card" style="left:150px">
    <div class="top"><span class="stars">★★★★★</span><span class="ago">18 hours ago</span></div>
    <h4>Excellent Services!</h4>
    <p>The parts arrived on time and in perfect condition. Their team was helpful and honest throughout the whole order.</p>
    <div class="who"><i></i>Harold Brenner</div>
  </div>
  <div class="abs card" style="left:450px;margin-left:0">
    <div class="top"><span class="stars">★★★★★</span><span class="ago">18 hours ago</span></div>
    <h4>Excellent Services!</h4>
    <p>Quick replies, fair prices and genuine spares. Our generator has run smoothly since the day it was fitted.</p>
    <div class="who"><i></i>Danny Ruskin</div>
  </div>
  <div class="abs card" style="left:750px">
    <div class="top"><span class="stars">★★★★★</span><span class="ago">18 hours ago</span></div>
    <h4>Excellent Services!</h4>
    <p>A dependable supplier for our fleet. Every engine part was checked, tested and delivered exactly as promised.</p>
    <div class="who"><i></i>Colin Ashby</div>
  </div>
</section>

<section class="abs contact">
  <h2 class="abs section-title">CONTACT US</h2>
  <p class="abs sub">Send us a message and our team will reply within one working day.</p>
  <div class="abs field" style="top:120px">Your Name*<svg class="ic" width="12" height="12" viewBox="0 0 12 12"><circle cx="6" cy="4" r="2.5" fill="#999"/><path d="M1 12 Q6 5 11 12Z" fill="#999"/></svg></div>
  <div class="abs field" style="top:192px">Your Email*<svg class="ic" width="12" height="12" viewBox="0 0 12 12"><rect x="0.5" y="2" width="11" height="8" fill="none" stroke="#999"/><polyline points="0.5,2 6,7 11.5,2" fill="none" stroke="#999"/></svg></div>
  <div class="abs field" style="top:264px">Your Subject<svg class="ic" width="12" height="12" viewBox="0 0 12 12"><line x1="1" y1="3" x2="11" y2="3" stroke="#999"/><line x1="1" y1="6" x2="11" y2="6" stroke="#999"/><line x1="1" y1="9" x2="8" y2="9" stroke="#999"/></svg></div>
  <div class="abs message">Your Message*</div>
  <div class="abs submit">SUBMIT</div>
</section>

<footer class="abs footer">
  <nav class="abs footer-nav"><span>HOME</span><span>ABOUT US</span><span>PRODUCTS &amp; STOCKS</span><span>CERTIFICATIONS &amp; QA</span><span>CONTACT US</span></nav>
  <div class="abs footer-rule"></div>
  <div class="abs brand"><i></i>VERODAK MARITIME BD (PVT.) LIMITED</div>
  <div class="abs socials">
    <i style="background:#1d6fa3"></i><i style="background:#3b5998"></i><i style="background:#c4302b"></i><i style="background:#2aa952"></i><i style="background:#7a4fa0"></i><i style="background:#2d9be0"></i><i style="background:#0a66c2"></i><i style="background:#d13f3f"></i>
  </div>
  <p class="abs disclaimer">Disclaimer: All trademarks and brand names shown on this site belong to their respective owners. We are not affiliated with any engine maker listed here.</p>
</footer>
<div class="abs copyright">Copyright © 2020 VERODAK MARITIME BD (PVT.) LIMITED. All Rights Reserved.</div>

</body>
</html>
```